Crestfield Row sign

24"x36" sign for new home construction job site. Located in affluent in-town neighborhood in Midwest. Traditional american style homes. 2nd generation construction company. Sign needs to convey strength and elegance but not overly elaborate. Competition most has signs consisting of text.

Sign text reads:
Crestfield Row Builders
Custom Luxury for Over 20 years
248-391-0827

Target Market(s)

Upper middle income home buyers

Industry/Entity Type

Construction

Font styles to use
Serif
Decorative

Requirements
Must have
• Logo image no more than 2 colors
Nice to have
• Should be visible and legible from distance of 30'
Should not have
• Not just image of house as logo

```html
<!DOCTYPE html>
<html lang="en">
<head>
<meta charset="utf-8">
<title>Crestfield Row Builders – Job Site Sign</title>
<link rel="stylesheet" href="https://fonts.googleapis.com/css2?family=Almendra:wght@700&family=Fondamento&family=Arimo:wght@700&display=swap">
<style>
  :root {
    --page-bg: #eef0f3;
    --crimson: #c8102e;
    --crimson-deep: #9e0b20;
    --gold: #e8b84a;
    --gold-light: #f9e29a;
    --gold-dark: #b07a1e;
    --cream: #fdf1dc;
    --cream-deep: #f6d9ad;
    --title-red: #c41230;
    --tagline-brown: #5a3210;
    --phone-ink: #1e1a16;
    --amber: #ffb300;
    --amber-deep: #f08c00;
  }
  * { margin: 0; padding: 0; box-sizing: border-box; }
  html, body {
    width: 1200px; height: 1000px; overflow: hidden;
    background: var(--page-bg);
  }
  .sign {
    position: absolute;
    left: 290px; top: 35px;
    width: 620px; height: 930px;
    background: linear-gradient(180deg, var(--crimson) 0%, var(--crimson-deep) 100%);
    overflow: hidden;
  }
  .ornament {
    position: absolute;
    left: 60px; width: 500px; height: 130px;
    border-radius: 65px;
    background: radial-gradient(ellipse at center, rgba(249,226,154,0.85) 0%, rgba(232,184,74,0.55) 45%, rgba(200,16,46,0) 75%);
  }
  .ornament--top { top: 70px; }
  .ornament--bottom { top: 770px; }
  .gold-band {
    position: absolute; left: 0; width: 100%;
    background: linear-gradient(180deg, var(--gold-light), var(--gold) 50%, var(--gold-dark));
  }
  .gold-band--top { top: 236px; height: 24px; }
  .gold-band--bottom { top: 700px; height: 8px; }
  .message-panel {
    position: absolute; left: 0; top: 260px;
    width: 100%; height: 440px;
    background: radial-gradient(ellipse at 50% 40%, #fffaf0 0%, var(--cream) 45%, var(--cream-deep) 100%);
  }
  .company-name {
    position: absolute; left: 0; top: 130px; width: 100%;
    text-align: center;
    font-family: "Almendra", Georgia, serif;
    font-weight: 700;
    font-size: 48px;
    color: var(--title-red);
  }
  .tagline {
    position: absolute; left: 0; top: 215px; width: 100%;
    text-align: center;
    font-family: "Fondamento", Georgia, serif;
    font-size: 33px;
    color: var(--tagline-brown);
  }
  .phone-pill {
    position: absolute; left: 45px; top: 640px;
    width: 530px; height: 92px;
    border-radius: 46px;
    border: 5px solid var(--gold-light);
    box-shadow: 0 0 0 3px var(--gold-dark);
    background: linear-gradient(180deg, #ffd54a 0%, var(--amber) 50%, var(--amber-deep) 100%);
    display: flex; align-items: center; justify-content: center;
  }
  .phone-number {
    font-family: "Arimo", Arial, sans-serif;
    font-weight: 700;
    font-size: 52px;
    color: var(--phone-ink);
    letter-spacing: 1px;
  }
</style>
</head>
<body>
  <main class="sign">
    <div class="ornament ornament--top" role="img" aria-label="Gold filigree scrollwork with a crowned shield crest at centre"></div>
    <div class="gold-band gold-band--top"></div>
    <section class="message-panel" role="img" aria-label="Cream panel with radiating sunburst rays">
      <h1 class="company-name">Crestfield Row Builders</h1>
      <p class="tagline">Custom Luxury for Over 20 years</p>
    </section>
    <div class="gold-band gold-band--bottom"></div>
    <div class="phone-pill"><span class="phone-number">248-391-0827</span></div>
    <div class="ornament ornament--bottom" role="img" aria-label="Gold filigree scrollwork ornament"></div>
  </main>
</body>
</html>
```